The Calder & Wimms Irish Bar Bendigo

I need an app for my local hotel/pub. We have a bistro, functions and live entertainment every week. I would like to promote meal deals, drink offers, upcoming shows, members benefits. I would need to be able to update daily. Thanks
Updates

Reason: I am away on holidays until 19th July and can only get contact rarely so follow up is only on my phone not computer. Thanks Gareth

Target Market(s)

18+

Industry/Entity Type

Entertainment

Requirements
Must have
• Promotions
Entertainment
Functions
About the hotel

```html
<!DOCTYPE html>
<html lang="en">
<head>
<meta charset="utf-8">
<title>The Calder &amp; Wimms Irish Bar – App Screens</title>
<link href="https://fonts.googleapis.com/css2?family=Bubblegum+Sans&family=Lato:wght@400;700&family=Dosis:wght@600&family=Gochi+Hand&display=swap" rel="stylesheet">
<style>
  :root{
    --bg-light:#f4f4f4;
    --bg-dark:#c9c9c9;
    --screen-top:#3a3a3a;
    --screen-bottom:#232323;
    --green-light:#7fbf7f;
    --green-mid:#3f8f4a;
    --green-dark:#1d5a28;
    --yellow:#f5e800;
    --yellow-line:#b8ab10;
    --white:#ffffff;
    --text-light:#e6e6e6;
    --price-grey:#a3a3a3;
    --offer-orange:#f7a21b;
    --offer-light:#ffc64a;
    --ink:#222222;
  }
  *{box-sizing:border-box;margin:0;padding:0}
  html,body{width:1200px;height:703px;overflow:hidden}
  body{background:radial-gradient(ellipse at 50% 35%,var(--bg-light) 0%,var(--bg-dark) 100%)}
  .stage{position:absolute;left:0;top:0;width:987px;height:578px;transform:scale(1.2158);transform-origin:0 0}

  .screen{position:absolute;overflow:hidden;
    background:radial-gradient(ellipse at 50% 20%,var(--screen-top) 0%,var(--screen-bottom) 90%);
    box-shadow:6px 8px 10px rgba(0,0,0,.45)}
  .screen--shows{left:52px;top:55px;width:279px;height:415px}
  .screen--drinks{left:398px;top:55px;width:278px;height:415px}
  .screen--drinks-scrolled{left:693px;top:58px;width:279px;height:416px}

  .app-header{position:absolute;left:0;top:0;right:0;height:36px;
    background:linear-gradient(to bottom,var(--green-light),var(--green-mid) 60%,var(--green-dark));
    z-index:3}
  .app-header::after{content:"";position:absolute;left:50%;bottom:-6px;margin-left:-6px;
    border-left:6px solid transparent;border-right:6px solid transparent;border-top:6px solid var(--green-dark)}
  .app-header h1{font:400 15px/36px "Bubblegum Sans",cursive;color:var(--white);text-align:center;letter-spacing:.3px;text-transform:uppercase}

  .tab-bar{position:absolute;left:0;right:0;bottom:0;height:40px;display:flex;
    background:linear-gradient(to bottom,var(--green-light),var(--green-mid) 45%,var(--green-dark))}
  .tab{flex:1;display:flex;align-items:center;justify-content:center;border-left:1px solid rgba(255,255,255,.35)}
  .tab:first-child{border-left:none}
  .tab svg{width:26px;height:28px}

  .timeline-rail{position:absolute;left:55px;top:36px;width:8px;height:339px;background:var(--yellow-line);
    box-shadow:inset 2px 0 0 rgba(255,255,255,.25)}
  .show{position:absolute;left:78px;color:var(--text-light);font:400 11px/14px "Lato",sans-serif}
  .show__dot{position:absolute;left:-27px;width:17px;height:17px;border-radius:50%;background:var(--yellow)}
  .show__date{font:400 10.5px/13px "Bubblegum Sans",cursive;color:var(--yellow);text-transform:uppercase;margin-bottom:5px}

  .drink-photo{position:absolute;border:1px solid #bbb}
  .drink-photo--margarita{left:14px;top:48px;width:150px;height:200px;
    background:linear-gradient(160deg,#8a8f96 0%,#d7b08f 35%,#e06a7a 55%,#55585c 100%)}
  .drink-photo--cocktails{left:0;top:47px;width:124px;height:202px;
    background:linear-gradient(160deg,#2a1a1a 0%,#c2262e 30%,#f2c94c 50%,#3fb8e0 70%,#3a1212 100%)}
  .offer-badge{position:absolute;width:88px;height:88px;border-radius:50%;
    background:radial-gradient(circle at 40% 35%,var(--offer-light),var(--offer-orange) 70%);
    border:2px solid #fff3d6;display:flex;align-items:center;justify-content:center;
    font:400 25px/1 "Bubblegum Sans",cursive;color:var(--white);z-index:2}
  .price{position:absolute;font:600 52px/1 "Dosis",sans-serif;color:var(--price-grey);text-shadow:2px 2px 3px rgba(0,0,0,.6)}
  .drink-copy{position:absolute;font:400 7.5px/11px "Lato",sans-serif;color:var(--text-light)}
  .scroll-track{position:absolute;left:0;top:341px;height:7px;background:var(--yellow-line);
    box-shadow:inset 0 2px 0 rgba(255,255,255,.25)}
  .scroll-knob{position:absolute;top:336px;width:16px;height:16px;border-radius:50%;background:var(--yellow)}
  .scroll-arrow{position:absolute;top:334px;right:0;width:0;height:0;
    border-top:11px solid transparent;border-bottom:11px solid transparent;border-left:14px solid var(--yellow)}

  .annotation{position:absolute;left:580px;top:537px;font:400 15px/1 "Gochi Hand",cursive;color:var(--ink);letter-spacing:1px;text-transform:uppercase}
  .annotation-arrow{position:absolute;left:675px;top:492px}
</style>
</head>
<body>
<div class="stage">

  <svg width="0" height="0" style="position:absolute">
    <defs>
      <symbol id="icon-dining" viewBox="0 0 26 28">
        <path d="M6 2v8M9 2v8M3 2v8q0 4 4.5 4.5V26" fill="none" stroke="currentColor" stroke-width="2.2" stroke-linecap="round"/>
        <path d="M19 26V2q-5 3-5 11h5" fill="currentColor"/>
      </symbol>
      <symbol id="icon-drinks" viewBox="0 0 26 28">
        <path d="M5 9h14l-2 17H7z" fill="currentColor"/>
        <path d="M12 12L20 2" stroke="currentColor" stroke-width="1.5"/>
        <circle cx="20" cy="6" r="3.2" fill="currentColor"/>
      </symbol>
      <symbol id="icon-shows" viewBox="0 0 26 28">
        <path d="M5 3l4 1 4 3 4-3 4-1-1 11 2 12H4l2-12z" fill="currentColor"/>
        <path d="M13 8v18" stroke="#2b6a34" stroke-width="1"/>
      </symbol>
      <symbol id="icon-members" viewBox="0 0 26 28">
        <circle cx="10" cy="11" r="5" fill="none" stroke="currentColor" stroke-width="1.6"/>
        <path d="M1.5 25q1-8 8.5-8t8.5 8z" fill="none" stroke="currentColor" stroke-width="1.6"/>
        <circle cx="17.5" cy="8.5" r="4.2" fill="none" stroke="currentColor" stroke-width="1.6"/>
        <path d="M19 15q5 1 6 8h-5" fill="none" stroke="currentColor" stroke-width="1.6"/>
      </symbol>
    </defs>
  </svg>

  <section class="screen screen--shows">
    <header class="app-header"><h1>Upcoming Shows</h1></header>
    <div class="timeline-rail"></div>
    <div class="show" style="top:78px">
      <span class="show__dot" style="top:12px"></span>
      <p class="show__date">Fry July 20</p>
      <p>The Australian DEAN<br>CARVER SHOW</p>
    </div>
    <div class="show" style="top:153px">
      <span class="show__dot" style="top:18px"></span>
      <p class="show__date">Fry Sept 7th</p>
      <p>Midnight on the Harbour<br>The Australian COPPER LANTERN<br>SHOW</p>
    </div>
    <div class="show" style="top:263px">
      <span class="show__dot" style="top:12px"></span>
      <p class="show__date">Fry July 20</p>
      <p>The Australian DEAN<br>CARVER SHOW</p>
    </div>
    <nav class="tab-bar">
      <div class="tab" style="color:var(--white)"><svg><use href="#icon-dining"/></svg></div>
      <div class="tab" style="color:var(--white)"><svg><use href="#icon-drinks"/></svg></div>
      <div class="tab" style="color:var(--yellow)"><svg><use href="#icon-shows"/></svg></div>
      <div class="tab" style="color:var(--white)"><svg><use href="#icon-members"/></svg></div>
    </nav>
  </section>

  <section class="screen screen--drinks">
    <header class="app-header"><h1>Drinks Offers</h1></header>
    <div class="drink-photo drink-photo--margarita" role="img" aria-label="Photo of a pink frozen cocktail at the bar taps"></div>
    <div class="offer-badge" style="left:136px;top:62px">OFFER</div>
    <div class="price" style="left:187px;top:172px">$6</div>
    <p class="drink-copy" style="left:18px;top:260px;width:242px">Lorem ipsum dolor sit amet, consectetur adipiscing elit. Donec aliquet pulvinar semper. Suspendisse iaculis euismod augue, nec hendrerit est vehicula id. Lorem ipsum dolor sit amet, consectetur adipiscing elit. Lorem ipsum dolor sit amet, consectetur adipiscing elit.</p>
    <div class="scroll-track" style="width:266px"></div>
    <div class="scroll-knob" style="left:134px"></div>
    <div class="scroll-arrow"></div>
    <nav class="tab-bar">
      <div class="tab" style="color:var(--white)"><svg><use href="#icon-dining"/></svg></div>
      <div class="tab" style="color:var(--yellow)"><svg><use href="#icon-drinks"/></svg></div>
      <div class="tab" style="color:var(--white)"><svg><use href="#icon-shows"/></svg></div>
      <div class="tab" style="color:var(--white)"><svg><use href="#icon-members"/></svg></div>
    </nav>
  </section>

  <section class="screen screen--drinks-scrolled">
    <header class="app-header"><h1>Drinks Offers</h1></header>
    <div class="drink-photo drink-photo--cocktails" role="img" aria-label="Photo of red and blue layered cocktails"></div>
    <div class="offer-badge" style="left:96px;top:61px">OFFER</div>
    <div class="price" style="left:147px;top:170px">$9</div>
    <p class="drink-copy" style="left:-4px;top:262px;width:244px">m ipsum dolor sit amet, consectetur adipiscing elit. Donec aliquet pulvinar semper. Suspendisse iaculis euismod augue, nec rerit est vehicula id. Lorem ipsum dolor sit amet, consectetur adipiscing elit. Lorem ipsum dolor sit amet, consectetur adipiscing elit.</p>
    <div class="scroll-track" style="width:266px;top:342px"></div>
    <div class="scroll-knob" style="left:79px;top:337px"></div>
    <div class="scroll-arrow" style="top:335px"></div>
    <nav class="tab-bar">
      <div class="tab" style="color:var(--white)"><svg><use href="#icon-dining"/></svg></div>
      <div class="tab" style="color:var(--yellow)"><svg><use href="#icon-drinks"/></svg></div>
      <div class="tab" style="color:var(--white)"><svg><use href="#icon-shows"/></svg></div>
      <div class="tab" style="color:var(--white)"><svg><use href="#icon-members"/></svg></div>
    </nav>
  </section>

  <svg class="annotation-arrow" width="50" height="42" viewBox="0 0 50 42">
    <path d="M6 38Q14 18 40 8" fill="none" stroke="var(--ink)" stroke-width="1.3"/>
    <path d="M30 6L41 8 35 16" fill="none" stroke="var(--ink)" stroke-width="1.3"/>
  </svg>
  <p class="annotation">When scrolling screen</p>
</div>
</body>
</html>
```